Visitenkarten für Familienunternehmen in den Bereichen Fliesen, Natursteine, Kaminöfen, Schwimmbäder und Whirlpools
Zielgruppe
Wir sind ein Familienunternehmen in dritter Generation und Spezialist für Fliesen, Natursteine, Kaminöfen, Schwimmbäder und Whirlpools. Professionell, kreativ und voller Leidenschaft begleiten wir unsere Kunden bei der Umsetzung ihrer Vorhaben. Von der persönlichen Beratung bis hin zur Ausführung profitieren unsere Kunden von qualifiziertem Fachpersonal und 60 Jahren Erfahrung. Unsere Zielgruppe sind Familien/Paare ab 35 Jahren, die Produkte höchster Qualität für Ihr Zuhause suchen.
Aufgabenstellung
Wir benötigen neue Visitenkarten, da wir ein neues Logo haben. Wir haben folgende Vorstellung:
Rückseite: Komplett schwarz bzw. dunkel (Farbton ähnlich DB703), mittig unser neues Logo in weiß.
Vorderseite: Auch hier Hintergrund schwarz, Logo in weiß, Name des Ansprechpartners samt Titel/Position, Firmenname, Adresse, Telefonnummer, eMail-Adresse und Social Media-Adresse. Des Weiteren sollte unser Portfolio aufgelistet sein (Fliesen, Natursteine, Kaminöfen, Schwimmbäder und Whirlpools). Alternativ können wir uns die Auflistung des Portfolios auch auf der Rückseite vorstellen. Alternativ können wir uns die Vorderseite auch in weiß mit schwarzer Schrift vorstellen.
Der Inhalt der Datei, welche am Ende erstellt wird, muss für unsere Druckerei editierbar sein (Schrift als Text, nicht als Pfad).
Ergänzung 25.03.2023:
Nachdem die ersten Design-Vorschläge eingetroffen sind, haben wir uns dazu entschieden, dass es eine Visitenkarte im Querformat sein soll. Vorder- und Rückseite vollen schwarz/dunkel sein.

```html
<!DOCTYPE html>
<html lang="de">
<head>
<meta charset="utf-8">
<title>Visitenkarten Stein-Brennor</title>
<link rel="stylesheet" href="https://fonts.googleapis.com/css2?family=Open+Sans:wght@400;700&display=swap">
<style>
  :root {
    --page-bg: #4b4b4c;
    --card-bg: #2b2a2a;
    --ink: #ffffff;
    --ink-soft: #e6e6e6;
  }
  * { box-sizing: border-box; margin: 0; padding: 0; }
  html, body {
    width: 1200px; height: 978px; overflow: hidden;
    background: var(--page-bg);
  }
  .sheet {
    position: relative; width: 1200px; height: 978px;
    display: flex; flex-direction: column; align-items: center;
    justify-content: center; gap: 34px;
  }
  .card {
    position: relative; width: 680px; height: 440px;
    background: var(--card-bg); color: var(--ink);
    font-family: "Open Sans", sans-serif;
    box-shadow: 0 10px 30px rgba(0,0,0,.35);
  }
  .brand-name {
    font-family: "Open Sans", sans-serif; font-weight: 400;
    color: var(--ink); white-space: nowrap;
  }

  /* Rückseite */
  .card-back .brand-name {
    position: absolute; left: 0; right: 0; top: 160px;
    text-align: center; font-size: 64px; line-height: 1;
  }
  .portfolio {
    position: absolute; left: 0; right: 0; bottom: 46px;
    text-align: center; font-size: 15px; letter-spacing: 1px;
    text-transform: uppercase; color: var(--ink-soft);
  }
  .portfolio .dot { margin: 0 6px; }

  /* Vorderseite */
  .card-front .brand-name {
    position: absolute; left: 48px; top: 268px;
    font-size: 34px; line-height: 1;
  }
  .divider {
    position: absolute; left: 362px; top: 110px;
    width: 1.5px; height: 230px; background: var(--ink);
  }
  .contact {
    position: absolute; left: 392px; top: 100px;
    font-size: 15.5px; line-height: 1.42; color: var(--ink-soft);
  }
  .contact .person { font-size: 21px; font-weight: 700; color: var(--ink); line-height: 1.2; }
  .contact .role { margin-bottom: 14px; }
  .contact .address { margin-bottom: 8px; }
  .contact-list { list-style: none; }
  .contact-list li { display: flex; align-items: center; gap: 12px; }
  .contact-list svg { width: 16px; height: 16px; flex: none; }
</style>
</head>
<body>
<main class="sheet">

  <section class="card card-back" aria-label="Rückseite">
    <div class="brand-name">Brennor</div>
    <p class="portfolio">
      Fliesen<span class="dot">•</span>Natursteine<span class="dot">•</span>Kaminöfen<span class="dot">•</span>Schwimmbäder<span class="dot">•</span>Whirlpools
    </p>
  </section>

  <section class="card card-front" aria-label="Vorderseite">
    <div class="brand-name">Brennor</div>
    <div class="divider"></div>
    <div class="contact">
      <p class="person">Matteo Brennor</p>
      <p class="role">Geschäftsführer</p>
      <p class="address">Stein-Brennor GmbH<br>Lindenweg 14<br>54321 Talheim</p>
      <ul class="contact-list">
        <li>
          <svg viewBox="0 0 16 16" aria-hidden="true"><path d="M4 1.5l2.2 3-1.3 1.6c.8 1.9 2.2 3.3 4 4.1l1.6-1.3 3 2.2-1.2 2.6C7 13.4 2.6 9 2.4 2.7z" fill="#fff"/></svg>
          <span>0 12 34 - 56 78 90</span>
        </li>
        <li>
          <svg viewBox="0 0 16 16" aria-hidden="true"><rect x="1.5" y="3.5" width="13" height="9" fill="none" stroke="#fff" stroke-width="1.3"/><path d="M1.5 3.5l6.5 5 6.5-5" fill="none" stroke="#fff" stroke-width="1.3"/></svg>
          <span>info@stein-brennor.de</span>
        </li>
        <li>
          <svg viewBox="0 0 16 16" aria-hidden="true"><circle cx="8" cy="8" r="6.3" fill="none" stroke="#fff" stroke-width="1.3"/><ellipse cx="8" cy="8" rx="2.7" ry="6.3" fill="none" stroke="#fff" stroke-width="1.1"/><path d="M1.7 8h12.6" stroke="#fff" stroke-width="1.1"/></svg>
          <span>www.stein-brennor.de</span>
        </li>
        <li>
          <svg viewBox="0 0 16 16" aria-hidden="true"><circle cx="8" cy="8" r="6" fill="#fff"/></svg>
          <span>@steinbrennor</span>
        </li>
      </ul>
    </div>
  </section>

</main>
</body>
</html>
```